Civil Engineering Web design

.Net Web design for a civil engineering company to include a blog page, I will like a site similar to this http://www.layoutgrove.example/demo/58273.html

company name: Dorvil Associates

-Civil/Structural Engineering Solutions

-Engineering Design Development and Consultancy

More Information about the internal pages or links:
1. Each one of the menu choices will take you to a page for that option where I will be able to insert text 2. Our team likewise should be a page with space for a photo of the staff and text space for inserting employee name and title, qualifications and job description and work experience...
Can we have 3 groups for these
Management Staff
Support Staff
Other Staff

3. The blog is a generic blog page where users can add comments to a any subjects raised by our team and submit... When they submit, the comments should be emailed to us 4. Contact us is also a tool for emailing us by users, whereby they provide their email, subject and email body 5. projects is a page that allows insertion of title, one photo and description of the project...
6. services is a page with links on the left for Construction Supervision Civil and Structured Engineering Designs Corporate Recognition

Each on when clicked should display the relevant information for the link which is a gallery of two photos side by side and one description per pair...

Industry/Entity Type

Construction

Requirements
Must have
• User ability to manage content; not design

Pages:
Home
Services
Projects (sub page picture gallery)
Reference
Our Team
Blog
Contact Us

```html
<!DOCTYPE html>
<html lang="en">
<head>
<meta charset="utf-8">
<title>Civil Engineering</title>
<link href="https://fonts.googleapis.com/css2?family=Open+Sans:wght@400;600;700&display=swap" rel="stylesheet">
<style>
:root{
  --orange:#f47a20;
  --orange-dark:#e0661a;
  --text:#555;
  --muted:#8a8a8a;
  --grey-box:#e4e4e4;
  --grey-btn:#bdbdbd;
  --line:#dcdcdc;
  --white:#fff;
  --caption-bg:rgba(40,40,40,.72);
}
*{margin:0;padding:0;box-sizing:border-box}
html,body{width:1200px;height:1145px;overflow:hidden}
body{position:relative;background:var(--white);font-family:"Open Sans",Arial,sans-serif;color:var(--text)}
.hero{position:absolute;left:0;top:0;width:1200px;height:545px;
  background:linear-gradient(90deg,#d9dde0 0%,#c3c9cf 30%,#8596a8 50%,#3c5579 70%,#6f8398 85%,#c9b27a 100%)}
.site-header{position:absolute;left:0;top:0;width:1200px;height:36px;background:rgba(255,255,255,.82)}
.brand{position:absolute;left:250px;top:6px;font-size:17px;font-weight:700;letter-spacing:1px;color:#333}
.main-nav{position:absolute;left:462px;top:0;display:flex;height:30px}
.main-nav a{display:block;padding:0 20px;line-height:30px;font-size:10px;color:#666;text-decoration:none}
.main-nav a.active{background:var(--orange);color:var(--white)}
.hero-caption{position:absolute;left:238px;top:230px;width:350px;height:175px;background:var(--caption-bg);padding:6px 12px;color:var(--white)}
.hero-caption h1{font-size:34px;font-weight:400;line-height:44px}
.hero-caption p{font-size:9.5px;line-height:13px;margin-top:2px;color:#e6e6e6}
.btn{display:inline-block;font-size:8px;font-weight:600;text-transform:uppercase;color:var(--white);text-align:center;line-height:18px;height:18px}
.btn-orange{background:var(--orange)}
.btn-grey{background:var(--grey-btn)}
.hero-caption .btn{margin-top:10px;width:100px}
.section-title{position:absolute;font-size:17px;font-weight:600;color:var(--orange);text-transform:uppercase}
.services-title{left:243px;top:582px}
.news-title{left:775px;top:582px}
.service{position:absolute;top:638px;width:168px;height:182px;text-align:center;padding-top:18px}
.service.featured{background:var(--grey-box)}
.service svg{display:block;margin:0 auto}
.service h3{font-size:10px;font-weight:600;color:#666;margin-top:8px}
.service p{font-size:8.5px;line-height:12px;color:var(--muted);padding:6px 24px 0}
.service .btn{width:104px;margin-top:10px}
.news-item{position:absolute;left:775px;width:190px;height:65px}
.news-thumb{position:absolute;left:0;top:0;width:60px;height:63px;background:linear-gradient(135deg,#d8a23a,#a0623a 60%,#6b5a4a)}
.news-body{position:absolute;left:68px;top:0;width:125px}
.news-body time{font-size:9px;color:#444;font-weight:600}
.news-body p{font-size:8.5px;line-height:11px;color:var(--muted);margin-top:2px}
.news-more{position:absolute;left:893px;top:798px;width:60px}
.team-heading{position:absolute;left:250px;top:852px;width:700px;height:26px}
.team-heading::before{content:"";position:absolute;left:0;right:0;top:13px;border-top:1px solid var(--line)}
.team-heading h2{position:relative;margin:0 auto;width:120px;background:var(--white);text-align:center;font-size:17px;font-weight:600;color:var(--orange)}
.team-member{position:absolute;top:897px;width:180px;text-align:center}
.team-photo{width:116px;height:116px;border-radius:50%;margin:0 auto;background:radial-gradient(circle at 50% 40%,#a9a29c,#4e4b4a 70%,#2b2b2b)}
.team-member time{display:block;font-size:9px;color:#444;font-weight:600;margin-top:6px}
.team-member p{font-size:8.5px;color:var(--muted);margin-top:2px}
.carousel-arrow{position:absolute;top:948px;width:40px;height:40px;border-radius:50%;background:#cfcfcf}
.carousel-arrow svg{display:block}
.site-footer{position:absolute;left:0;top:1095px;width:1200px;height:50px;background:var(--orange);text-align:center;line-height:50px;font-size:9px;color:var(--white)}
</style>
</head>
<body>
<div class="hero" role="img" aria-label="Photo of a smiling engineer in navy overalls holding a blue hard hat inside a bright industrial warehouse"></div>

<header class="site-header">
  <div class="brand">CIVIL ENGINEERING</div>
  <nav class="main-nav">
    <a class="active" href="#">Home</a><a href="#">Services</a><a href="#">Projects</a><a href="#">Reference</a><a href="#">Our Team</a><a href="#">Blog</a><a href="#">Contact Us</a>
  </nav>
</header>

<div class="hero-caption">
  <h1>Civil Engineering....</h1>
  <p>Lorem ipsum is simply dummy text of the printing and typesetting industry. Lorem ipsum has been the industry's standard dummy text ever since, when an unknown printer took a galley of type and scrambled it to make a type specimen book.</p>
  <span class="btn btn-orange">Read more</span>
</div>

<h2 class="section-title services-title">Our Servies</h2>

<div class="service featured" style="left:238px">
  <svg width="56" height="56" viewBox="0 0 56 56"><circle cx="28" cy="28" r="27" fill="#fff"/><circle cx="28" cy="28" r="18" fill="var(--orange)"/><path d="M18 30h20v4H18zM22 22h12v5H22z" fill="#fff"/></svg>
  <h3>Project Management</h3>
  <p>Lorem ipsum is simply dummy text of the printing and typesetting industry.</p>
  <span class="btn btn-orange">Read more</span>
</div>
<div class="service" style="left:418px">
  <svg width="56" height="56" viewBox="0 0 56 56"><circle cx="28" cy="28" r="27" fill="#e6e6e6"/><rect x="20" y="15" width="16" height="27" fill="#b5b5b5"/><path d="M23 19h3v3h-3zM30 19h3v3h-3zM23 26h3v3h-3zM30 26h3v3h-3zM23 33h3v3h-3zM30 33h3v3h-3z" fill="#fff"/></svg>
  <h3>Construction</h3>
  <p>Lorem ipsum is simply dummy text of the printing and typesetting industry.</p>
  <span class="btn btn-grey">Read more</span>
</div>
<div class="service" style="left:582px">
  <svg width="56" height="56" viewBox="0 0 56 56"><circle cx="28" cy="28" r="27" fill="#e6e6e6"/><circle cx="26" cy="26" r="9" fill="none" stroke="#b5b5b5" stroke-width="4"/><path d="M32 32l9 9" stroke="#b5b5b5" stroke-width="5" stroke-linecap="round"/></svg>
  <h3>Speciality services</h3>
  <p>Lorem ipsum is simply dummy text of the printing and typesetting industry.</p>
  <span class="btn btn-grey">Read more</span>
</div>

<h2 class="section-title news-title">Our News</h2>
<article class="news-item" style="top:630px">
  <div class="news-thumb" role="img" aria-label="Photo of construction workers on site"></div>
  <div class="news-body"><time>23/05/2014</time><p>Lorem ipsum is simply dummy text of the printing and typesetting industry.</p></div>
</article>
<article class="news-item" style="top:714px">
  <div class="news-thumb" role="img" aria-label="Photo of a worker with machinery"></div>
  <div class="news-body"><time>23/05/2014</time><p>Lorem ipsum is simply dummy text of the printing and typesetting industry.</p></div>
</article>
<span class="btn btn-orange news-more">More</span>

<div class="team-heading"><h2>OUR TEAM</h2></div>

<div class="carousel-arrow" style="left:248px"><svg width="40" height="40" viewBox="0 0 40 40"><path d="M23 13l-7 7 7 7" fill="none" stroke="#fff" stroke-width="3"/></svg></div>
<div class="carousel-arrow" style="left:918px"><svg width="40" height="40" viewBox="0 0 40 40"><path d="M17 13l7 7-7 7" fill="none" stroke="#fff" stroke-width="3"/></svg></div>

<div class="team-member" style="left:318px">
  <div class="team-photo" role="img" aria-label="Portrait photo of a team member"></div>
  <time>23/05/2014</time><p>Lorem ipsum is simply dummy text of printing</p>
</div>
<div class="team-member" style="left:510px">
  <div class="team-photo" role="img" aria-label="Portrait photo of a team member"></div>
  <time>23/05/2014</time><p>Lorem ipsum is simply dummy text of printing</p>
</div>
<div class="team-member" style="left:698px">
  <div class="team-photo" role="img" aria-label="Portrait photo of a team member"></div>
  <time>23/05/2014</time><p>Lorem ipsum is simply dummy text of printing</p>
</div>

<footer class="site-footer">Copyright © 2014 Civil Engineering</footer>
</body>
</html>
```